Business Card Design- Mortgage Firm

Looking to design a business Card for our Outside sales people. This card is used to provide their contact information to prospective clients and realtors. Must have All Pertinent company and licensing information by law. We are looking for a very modern design that flows with our current logo color scheme. Red/White/Black

Industry/Entity Type

Mortgage Lender

Contact Information for Business Card

Must stick with current color scheme.

Colors
f04a50
ffffff
ecf7fb

Requirements
Must have
• Company Logo or similar
• Company Address (547 W Larkin Avenue, Suite 318, Fairhaven CA 92877 NMLS: 2947163)
• Agent Name (Nora Pell)
• Title (Senior Mortgage Loan Originator)
• NMLS# 7395281
• Toll Free: 800-627-3184
• Direct : 310-555-8347
Nice to have
• Room for Agent Picture

```html
<!DOCTYPE html>
<html lang="en">
<head>
<meta charset="utf-8">
<title>Halden Mortgage – Business Card</title>
<link rel="stylesheet" href="https://fonts.googleapis.com/css2?family=Montserrat:wght@700;800&family=Roboto:wght@400;500&display=swap">
<style>
  :root {
    --brand-red: #c1000b;
    --card-white: #ffffff;
    --ink: #141414;
    --backdrop: #ecefef;
    --shadow: rgba(0, 0, 0, 0.14);
  }
  * { box-sizing: border-box; margin: 0; padding: 0; }
  html, body {
    width: 1200px;
    height: 800px;
    overflow: hidden;
    background: var(--backdrop);
  }
  .canvas {
    position: relative;
    width: 1200px;
    height: 800px;
  }
  .card {
    position: absolute;
    top: 252px;
    width: 520px;
    height: 297px;
    background: var(--card-white);
    border-radius: 4px;
    box-shadow: 0 10px 28px var(--shadow);
    overflow: hidden;
  }

  /* Back side: company name and address */
  .card--back { left: 60px; }
  .brand-lockup {
    position: absolute;
    top: 108px;
    left: 0;
    width: 100%;
    display: flex;
    justify-content: center;
    align-items: center;
    gap: 16px;
  }
  .brand-lockup__square {
    width: 58px;
    height: 58px;
    background: var(--brand-red);
  }
  .brand-lockup__name {
    font-family: "Montserrat", sans-serif;
    font-weight: 800;
    font-size: 34px;
    letter-spacing: 1px;
    color: var(--brand-red);
    line-height: 1;
  }
  .company-address {
    position: absolute;
    bottom: 30px;
    left: 0;
    width: 100%;
    text-align: center;
    font-family: "Roboto", sans-serif;
    font-size: 12.5px;
    color: var(--ink);
  }

  /* Front side: agent details */
  .card--front { left: 620px; }
  .accent-panel {
    position: absolute;
    inset: 0;
    width: 520px;
    height: 297px;
  }
  .front-brand {
    position: absolute;
    top: 24px;
    left: 34px;
    display: flex;
    align-items: center;
    gap: 10px;
  }
  .front-brand__circle {
    width: 46px;
    height: 46px;
    border-radius: 50%;
    background: var(--brand-red);
  }
  .front-brand__name {
    font-family: "Montserrat", sans-serif;
    font-weight: 800;
    font-size: 14px;
    color: var(--brand-red);
    letter-spacing: 0.5px;
  }
  .agent {
    position: absolute;
    top: 104px;
    left: 34px;
    font-family: "Roboto", sans-serif;
    color: var(--ink);
  }
  .agent__name {
    font-family: "Montserrat", sans-serif;
    font-weight: 800;
    font-size: 21px;
    letter-spacing: 1px;
    color: var(--brand-red);
    margin-bottom: 4px;
  }
  .agent__title, .agent__license {
    font-size: 15px;
    line-height: 19px;
  }
  .agent__contacts {
    margin-top: 14px;
    font-size: 15px;
    line-height: 19px;
  }
  .agent__label { color: var(--brand-red); }
</style>
</head>
<body>
<main class="canvas">

  <section class="card card--back" aria-label="Business card, company side">
    <div class="brand-lockup">
      <span class="brand-lockup__square"></span>
      <span class="brand-lockup__name">HALDEN MORTGAGE</span>
    </div>
    <p class="company-address">547 W Larkin Avenue, Suite 318, Fairhaven CA 92877 NMLS: 2947163</p>
  </section>

  <section class="card card--front" aria-label="Business card, agent side">
    <svg class="accent-panel" viewBox="0 0 520 297" aria-hidden="true">
      <path d="M350 0 H520 V297 H335 V150 L343 150 Q350 150 350 143 Z" fill="var(--brand-red)"/>
      <rect x="488" y="0" width="14" height="200" fill="var(--card-white)"/>
    </svg>

    <div class="front-brand">
      <span class="front-brand__circle"></span>
      <span class="front-brand__name">HALDEN MORTGAGE</span>
    </div>

    <div class="agent">
      <h1 class="agent__name">NORA PELL</h1>
      <p class="agent__title">Senior Mortgage Loan Originator</p>
      <p class="agent__license">NMLS# 7395281</p>
      <div class="agent__contacts">
        <p><span class="agent__label">Toll Free:</span> 800-627-3184</p>
        <p><span class="agent__label">Direct</span> : 310-555-8347</p>
        <p>www.haldenmortgage.com</p>
      </div>
    </div>
  </section>

</main>
</body>
</html>
```